Business Card Design

We are a residential half way house for the addict ,the alcoholic and dual diagnosed in recovery.
i house both men and woman age 18+

Industry/Entity Type

Residential

```html
<!DOCTYPE html>
<html lang="en">
<head>
<meta charset="utf-8">
<title>Renewal Path Sober House – Business Card</title>
<link rel="stylesheet" href="https://fonts.googleapis.com/css2?family=Jost:wght@400;500&family=Oswald:wght@500&display=swap">
<style>
  :root {
    --backdrop: #d9d9db;
    --card: #1d1d1d;
    --accent: #f37021;
    --shadow: rgba(0, 0, 0, 0.28);
  }
  * { margin: 0; padding: 0; box-sizing: border-box; }
  html, body {
    width: 1200px;
    height: 834px;
    overflow: hidden;
    background: var(--backdrop);
  }
  .canvas {
    width: 1200px;
    height: 834px;
    display: flex;
    align-items: center;
    justify-content: center;
  }
  .business-card {
    position: relative;
    width: 735px;
    height: 420px;
    background: var(--card);
    box-shadow: 0 18px 40px var(--shadow);
    color: var(--accent);
    font-family: "Jost", "Futura", sans-serif;
    overflow: hidden;
  }
  .name-bar {
    position: absolute;
    left: 0;
    top: 86px;
    width: 118px;
    height: 32px;
    background: var(--accent);
  }
  .holder {
    position: absolute;
    left: 134px;
    top: 58px;
  }
  .holder-name {
    font-size: 32px;
    font-weight: 400;
    line-height: 1.1;
    letter-spacing: 0.5px;
  }
  .holder-role,
  .holder-note {
    font-size: 15px;
    line-height: 1.35;
  }
  .holder-role { margin-top: 6px; }
  .email {
    position: absolute;
    left: 34px;
    top: 168px;
    display: flex;
    align-items: center;
    gap: 12px;
    font-size: 16px;
  }
  .icon-badge {
    width: 30px;
    height: 30px;
    flex: none;
  }
  .company {
    position: absolute;
    left: 392px;
    top: 52px;
  }
  .company-name {
    font-family: "Oswald", "Arial Narrow", sans-serif;
    font-weight: 500;
    font-size: 25px;
    text-transform: uppercase;
    letter-spacing: 0.3px;
    line-height: 1.15;
  }
  .company-address {
    font-size: 15px;
    margin-top: 6px;
  }
  .feature-bar {
    position: absolute;
    left: 318px;
    top: 150px;
    right: 0;
    height: 54px;
    background: var(--accent);
  }
  .phones {
    position: absolute;
    left: 432px;
    top: 246px;
    display: flex;
    gap: 18px;
    align-items: flex-start;
  }
  .phones .icon-badge { margin-top: 4px; }
  .phone-list {
    list-style: none;
    font-size: 19px;
    line-height: 1.4;
    letter-spacing: 0.4px;
  }
</style>
</head>
<body>
<main class="canvas">
  <article class="business-card">
    <div class="name-bar"></div>

    <section class="holder">
      <h1 class="holder-name">Marisa Delgado</h1>
      <p class="holder-role">Owner</p>
      <p class="holder-note">(15 yrs.in recovery)</p>
    </section>

    <p class="email">
      <svg class="icon-badge" viewBox="0 0 30 30" aria-hidden="true">
        <circle cx="15" cy="15" r="15" fill="var(--accent)"/>
        <rect x="8" y="10" width="14" height="10" rx="1" fill="var(--card)"/>
        <path d="M8.5 10.5 L15 15.5 L21.5 10.5" fill="none" stroke="var(--accent)" stroke-width="1.3"/>
      </svg>
      <span>marisadelgado@example.com</span>
    </p>

    <section class="company">
      <h2 class="company-name">Renewal Path Sober House Inc.</h2>
      <p class="company-address">2180 Palm Grove Rd. Bayview, Fla 33990</p>
    </section>

    <div class="feature-bar"></div>

    <section class="phones">
      <svg class="icon-badge" viewBox="0 0 30 30" aria-hidden="true">
        <circle cx="15" cy="15" r="15" fill="var(--accent)"/>
        <path d="M11 8 L13.5 8 L14.5 11.5 L12.8 12.8 C13.6 14.8 15.2 16.4 17.2 17.2 L18.5 15.5 L22 16.5 L22 19 C22 20.2 21 21 19.8 21 C14 20.6 9.4 16 9 10.2 C9 9 9.8 8 11 8 Z" fill="var(--card)"/>
      </svg>
      <ul class="phone-list">
        <li>(555) 014-2207</li>
        <li>(555) 014-2208</li>
        <li>Fax (555) 014-7731</li>
      </ul>
    </section>
  </article>
</main>
</body>
</html>
```